Silver Ridge Business Card Design

I have an existing corporate logo. I'd like to clean it up bit (sharpen it up) and make it look better (without major redesign). I'd like to get the logo itself in all major file formats for print, web, etc.
Then I'd like a business card design that reflects a strategy consulting firm. It should be clean - logo and text without major graphics, and perhaps some small color treatments that match the logo color. The card should suggest high quality in terms of the company.
I'd like the files for card in all major print formats.
Target Market(s)
Silver Ridge Partners is a strategy development and business consulting firm focused on small to mid-sized companies. We specialize in business strategy, comprehensive business plan development, market segmentation and positioning, financial models, marketing and sales strategy, product strategy and the effective use of social media in business growth. We operate as consultants, advisers, retained members of management teams, and Board members. We often serve in the role of Chief Strategy Officer, supporting CEO's and other senior executives to enhance top and bottom line growth.
Our overall approach with clients is to deliver actual results, and we often take an active team role with business founders and management teams to drive business growth and affect real changes in performance. As a result, we approach each situation uniquely and partner with clients in a manner that will have the biggest impact on enterprise value.
Business
Look and feel

```html
<!DOCTYPE html>
<html lang="en">
<head>
<meta charset="utf-8">
<title>Silver Ridge Partners – Business Card</title>
<link rel="stylesheet" href="https://fonts.googleapis.com/css2?family=PT+Sans:wght@400;700&display=swap">
<style>
  :root {
    --backdrop: #3b3735;
    --card: #f7f7f6;
    --card-shade: #e9eaeb;
    --brand-navy: #12398a;
    --accent-orange: #e0451b;
    --ink: #1d1d1d;
    --icon-grey: #a6a6a6;
    --rule-grey: #b9b9b9;
  }
  html, body {
    margin: 0;
    width: 1200px;
    height: 1200px;
    overflow: hidden;
    background: var(--backdrop);
    font-family: "PT Sans", sans-serif;
  }
  .card {
    position: absolute;
    left: 80px;
    top: 300px;
    width: 1040px;
    height: 600px;
    background: linear-gradient(160deg, var(--card) 55%, var(--card-shade) 100%);
    box-shadow: 0 14px 40px rgba(0,0,0,0.45);
  }
  .brand {
    position: absolute;
    left: 70px;
    top: 80px;
    display: flex;
    align-items: center;
    gap: 16px;
  }
  .brand-dot {
    width: 34px;
    height: 34px;
    border-radius: 50%;
    background: var(--brand-navy);
  }
  .brand-name {
    font-weight: 700;
    font-size: 34px;
    line-height: 1.05;
    color: var(--brand-navy);
    text-transform: uppercase;
    letter-spacing: 0.5px;
  }
  .person {
    position: absolute;
    left: 70px;
    top: 270px;
    color: var(--accent-orange);
    font-size: 33px;
    line-height: 1.2;
  }
  .address {
    position: absolute;
    left: 70px;
    top: 375px;
    color: var(--ink);
    font-size: 30px;
    line-height: 1.25;
  }
  .icon-rail {
    position: absolute;
    left: 480px;
    top: 60px;
    width: 90px;
    height: 470px;
    border-left: 3px dashed var(--rule-grey);
    border-right: 3px dashed var(--rule-grey);
  }
  .contact-list {
    position: absolute;
    left: 480px;
    top: 70px;
    margin: 0;
    padding: 0;
    list-style: none;
  }
  .contact-item {
    display: flex;
    align-items: center;
    height: 90px;
  }
  .contact-icon {
    width: 96px;
    display: flex;
    justify-content: center;
  }
  .contact-icon svg { width: 48px; height: 48px; }
  .contact-text {
    margin-left: 30px;
    font-size: 30px;
    color: var(--ink);
    letter-spacing: 0.3px;
  }
</style>
</head>
<body>
  <section class="card" aria-label="Silver Ridge Partners business card">
    <div class="brand">
      <span class="brand-dot"></span>
      <span class="brand-name">Silver Ridge<br>Partners</span>
    </div>

    <div class="person">
      <div class="person-name">Daniel M. Hartwell</div>
      <div class="person-title">Partner and Founder</div>
    </div>

    <div class="address">
      412 Alder Crest Lane<br>
      Fairmont, Illinois 60499
    </div>

    <div class="icon-rail"></div>

    <ul class="contact-list">
      <li class="contact-item">
        <span class="contact-icon">
          <svg viewBox="0 0 48 48" aria-hidden="true">
            <path d="M6 16c0-5 8-8 18-8s18 3 18 8v4h-9v-4c-3-1-6-1.5-9-1.5s-6 .5-9 1.5v4H6z" fill="var(--icon-grey)"/>
            <path d="M12 22h24l4 18H8z" fill="var(--icon-grey)"/>
            <circle cx="24" cy="31" r="5" fill="var(--card)"/>
          </svg>
        </span>
        <span class="contact-text">312.555.0148</span>
      </li>
      <li class="contact-item">
        <span class="contact-icon">
          <svg viewBox="0 0 48 48" aria-hidden="true">
            <text x="24" y="38" text-anchor="middle" font-family="PT Sans, sans-serif" font-size="44" font-weight="700" fill="var(--icon-grey)">@</text>
          </svg>
        </span>
        <span class="contact-text">dan@srpartners.com</span>
      </li>
      <li class="contact-item">
        <span class="contact-icon">
          <svg viewBox="0 0 48 48" aria-hidden="true" fill="none" stroke="var(--icon-grey)" stroke-width="3">
            <circle cx="24" cy="24" r="19"/>
            <ellipse cx="24" cy="24" rx="8" ry="19"/>
            <line x1="5" y1="24" x2="43" y2="24"/>
            <path d="M9 14h30M9 34h30"/>
          </svg>
        </span>
        <span class="contact-text">srpartners.com</span>
      </li>
      <li class="contact-item">
        <span class="contact-icon">
          <svg viewBox="0 0 48 48" aria-hidden="true">
            <rect x="5" y="5" width="38" height="38" rx="4" fill="var(--icon-grey)"/>
          </svg>
        </span>
        <span class="contact-text">profiles.net/in/dhartwell/</span>
      </li>
      <li class="contact-item">
        <span class="contact-icon">
          <svg viewBox="0 0 48 48" aria-hidden="true">
            <circle cx="24" cy="24" r="18" fill="var(--icon-grey)"/>
          </svg>
        </span>
        <span class="contact-text">@DanHartwell</span>
      </li>
    </ul>
  </section>
</body>
</html>
```